Business card design needed

My business is in Matchmaking. My objective is to find the most compatible partner for my clients....basically I'm in the love and happiness industry bringing two people together for a lasting loving relationship.

I envision the design to be something with 2 people who are in love looking happy or even a silhouette.....I don't really know, I'm open to ideas.....maybe no picture at all, but I want it to be classy :-)

I do have a logo which I will upload. You can also go to my website to give you an idea on the colours and the design if that helps, however the website is not finished yet, it should be up by today or tomorrow. If the website has a heart with swirls on the upper left hand corner, that is the old website, please ignore that one. The one that will be up shortly has a picture frame on the home page with my logo that will be in the file I will upload on this page.

Target Market(s)

There are three categories: Over 45, Asian and Western and same sex, but would be able to afford to hire a matchmaker

Contact Information for Business Card

The Tide Lantern
Helping You Find The "One"
Mira Feltham
Matchmaker
0472 915 264
info@thetidelantern.com.au
www.thetidelantern.com.au

```html
<!DOCTYPE html>
<html lang="en">
<head>
<meta charset="utf-8">
<title>The Tide Lantern – Business Card</title>
<link rel="stylesheet" href="https://fonts.googleapis.com/css2?family=Open+Sans:wght@400;600;700&display=swap">
<style>
  :root {
    --backdrop: #f9ad62;
    --card: #fbfbfa;
    --mauve: #8b6b7b;
    --mauve-light: #b39aa6;
    --mauve-deep: #7a5b6b;
    --ink-grey: #7b7478;
    --ribbon: #9a7a8a;
    --white: #ffffff;
  }
  * { box-sizing: border-box; margin: 0; padding: 0; }
  html, body {
    width: 1200px; height: 1023px; overflow: hidden;
    background: var(--backdrop);
    font-family: "Open Sans", Arial, sans-serif;
  }
  .card {
    position: absolute; left: 120px; top: 237px;
    width: 960px; height: 549px;
    background: var(--card);
    border-radius: 6px;
    box-shadow: 0 18px 40px rgba(120, 70, 20, 0.28);
    overflow: hidden;
  }
  .couple-illustration {
    position: absolute; left: 0; top: 0;
    width: 480px; height: 549px;
    background: linear-gradient(160deg, var(--mauve-light) 0%, var(--mauve) 55%, var(--mauve-deep) 100%);
    clip-path: polygon(0 22%, 38% 14%, 62% 0, 100% 0, 100% 100%, 0 100%);
  }
  .website {
    position: absolute; left: 40px; bottom: 36px;
    color: var(--white); font-size: 24px; letter-spacing: 0.5px;
  }
  .details {
    position: absolute; left: 530px; top: 56px; width: 400px;
    color: var(--ink-grey);
  }
  .brand {
    display: flex; align-items: center; gap: 14px;
    font-size: 34px; font-weight: 400; color: var(--ink-grey);
  }
  .brand-dot {
    width: 22px; height: 22px; border-radius: 50%;
    background: var(--mauve-light); flex: none;
  }
  .person-name {
    margin-top: 34px;
    font-size: 42px; font-weight: 700; color: var(--mauve);
    line-height: 1.1;
  }
  .role { font-size: 22px; margin-top: 4px; }
  .ribbon { position: relative; margin-top: 26px; width: 380px; height: 62px; }
  .ribbon svg { position: absolute; inset: 0; }
  .ribbon-text {
    position: absolute; left: 0; right: 0; top: 17px;
    text-align: center; color: var(--white); font-size: 18px;
  }
  .phone {
    margin-top: 36px; font-size: 36px; font-weight: 700; color: var(--mauve-deep);
  }
  .email { margin-top: 16px; font-size: 22px; }
</style>
</head>
<body>
  <main class="card">
    <div class="couple-illustration" role="img" aria-label="Mauve silhouette illustration of a couple about to kiss"></div>
    <p class="website">www.thetidelantern.com.au</p>

    <section class="details">
      <div class="brand"><span class="brand-dot"></span>The Tide Lantern</div>
      <h1 class="person-name">Mira Feltham</h1>
      <p class="role">Matchmaker</p>
      <div class="ribbon">
        <svg viewBox="0 0 380 62" width="380" height="62" aria-hidden="true">
          <polygon points="0,12 34,12 34,58 0,58 14,35" fill="var(--mauve-deep)"/>
          <polygon points="380,12 346,12 346,58 380,58 366,35" fill="var(--mauve-deep)"/>
          <rect x="24" y="4" width="332" height="46" fill="var(--ribbon)"/>
        </svg>
        <p class="ribbon-text">Helping You Find The 1</p>
      </div>
      <p class="phone">0472 915 264</p>
      <p class="email">info@thetidelantern.com.au</p>
    </section>
  </main>
</body>
</html>
```